PlexoVane - Risk Analysis Software For the Petroleum Professional

We are a small niche software engineering firm delivering innovative software products for the Energy Industry and have been in business since 2002. For the immediate task I am looking for a professional landing page for one of our software products (PlexoVaneĀ®) that will attract new clients and promote sales leads.
Secondarily (as a follow up) I am also looking for a new website design. The current website we have is very outdated so I am also looking for the landing page design to feed into a contemporary web site with a similar design as the landing page. Maybe I am going about this backwards? I will look for your recommendations. I estimate 4 to 5 pages are needed for the new website, one will contain a form for collecting client inquiries. Here is a link to a form that I have used in the past.
https://www.plexovane-demo.net/request1.html
The form should append new records to a database and generate an email to the client for acknowledgement and finish with a confirmation page or equivalent effect.
Our current provider is Harbor Gridworks (or Hostlyx.net).
https://www.plexovane-demo.net/
I have many JPG images of screen shots and presentation images and I want to be able to circulate these images on my end after the page has been constructed. So (when possible) the images that are used within the page(s) need to be referenced individually.
The web page(s) need to be view compatible on all devices. Windows, Mac, ios iPhone and iPad and Android.
PlexoVaneĀ® is a US registered trademark.
Uploaded is a short PowerPoint Slide presentation.
Note: The company that owns this software is my company called PlexoVane, LLC
Updates
Confirming....This project is for a landing page design with its HTML/CSS files and referenced images.
Target Market(s)
Oil Companies
Industry/Entity Type
Energy
Font styles to use
Colors
Designer to choose colors to be used in the design.
Look and feel
Each slider illustrates characteristics of the customer's brand and the style your logo design should communicate.

```html
<!DOCTYPE html>
<html lang="en">
<head>
<meta charset="utf-8">
<title>PlexoVane – Banners</title>
<link href="https://fonts.googleapis.com/css2?family=Montserrat:wght@400;500;600;700;800&display=swap" rel="stylesheet">
<style>
  :root {
    --page-bg: #ffffff;
    --title-grey: #a8a8a8;
    --text-white: #ffffff;
    --red-bright: #e0141a;
    --red-mid: #b30d12;
    --red-deep: #5e0508;
    --near-black: #120203;
  }
  * { box-sizing: border-box; margin: 0; padding: 0; }
  html, body {
    width: 1200px;
    height: 2883px;
    overflow: hidden;
    background: var(--page-bg);
    font-family: "Montserrat", Arial, sans-serif;
  }
  .sheet { position: relative; width: 1200px; height: 2883px; }
  .sheet-title {
    position: absolute;
    top: 34px; left: 0; width: 100%;
    text-align: center;
    font-size: 82px;
    font-weight: 700;
    letter-spacing: 3px;
    color: var(--title-grey);
    line-height: 1;
    padding-left: 20px;
  }
  .banner {
    position: absolute;
    left: 0;
    width: 1200px;
    height: 624px;
    overflow: hidden;
    color: var(--text-white);
  }
  .banner-1 { top: 148px; }
  .banner-2 { top: 797px; }
  .banner-3 { top: 1469px; }
  .banner-4 { top: 2166px; }
  .banner-photo { position: absolute; inset: 0; }
  .banner-1 .banner-photo {
    background:
      radial-gradient(ellipse at 75% 30%, rgba(255,40,40,0.55), transparent 60%),
      linear-gradient(100deg, var(--near-black) 0%, var(--red-deep) 25%, var(--red-mid) 55%, var(--red-bright) 100%);
  }
  .banner-2 .banner-photo {
    background:
      linear-gradient(180deg, var(--near-black) 0%, var(--red-deep) 22%, var(--red-mid) 55%, var(--red-bright) 80%, var(--red-mid) 100%);
  }
  .banner-3 .banner-photo {
    background:
      radial-gradient(ellipse at 60% 25%, rgba(255,120,120,0.45), transparent 55%),
      linear-gradient(180deg, var(--red-bright) 0%, var(--red-mid) 50%, var(--red-deep) 85%, var(--near-black) 100%);
  }
  .banner-4 .banner-photo {
    background:
      radial-gradient(ellipse at 90% 95%, rgba(255,90,40,0.55), transparent 45%),
      linear-gradient(100deg, var(--near-black) 0%, var(--red-deep) 20%, var(--red-mid) 55%, var(--red-bright) 100%);
  }
  .banner-content {
    position: absolute;
    left: 0; top: 128px;
    width: 100%;
    text-align: center;
  }
  .banner-2 .banner-content, .banner-4 .banner-content { left: 6px; }
  .banner-3 .banner-content { left: 4px; top: 122px; }
  .brand-name {
    display: inline-block;
    position: relative;
    font-size: 62px;
    font-weight: 800;
    line-height: 1;
    letter-spacing: -1px;
  }
  .brand-name sup {
    position: absolute;
    top: -8px; right: -26px;
    font-size: 24px;
    font-weight: 800;
  }
  .headline {
    margin-top: 18px;
    font-size: 32px;
    font-weight: 600;
    line-height: 35px;
    letter-spacing: 0.5px;
  }
  .summary {
    width: 750px;
    margin: 10px auto 0;
    font-size: 14px;
    line-height: 21px;
    font-weight: 400;
  }
  .summary sup { font-size: 8px; }
  .cta {
    display: inline-block;
    margin-top: 22px;
    width: 141px;
    height: 40px;
    line-height: 36px;
    border: 2px solid var(--text-white);
    border-radius: 2px;
    color: var(--text-white);
    text-decoration: none;
    font-size: 12px;
    font-weight: 700;
  }
</style>
</head>
<body>
<main class="sheet">
  <h1 class="sheet-title">BANNERS</h1>

  <section class="banner banner-1">
    <div class="banner-photo" role="img" aria-label="Offshore jack-up drilling rig and supply vessel at sea under a red overlay with stock chart lines"></div>
    <div class="banner-content">
      <div class="brand-name">PlexoVane<sup>®</sup></div>
      <h2 class="headline">RISK ANALYSIS SOFTWARE<br>FOR THE PETROLEUM PROFESSIONAL</h2>
      <p class="summary">PlexoVane<sup>®</sup> offers the petroleum industry a powerful, yet easy-to-use, well cost and scheduling risk analysis software. Our unique and intuitive user interface is designed specifically for the petroleum professional and offers an efficient and consistent way to create an accurate risked drilling and completion AFE.</p>
      <a class="cta" href="#">LEARN MORE</a>
    </div>
  </section>

  <section class="banner banner-2">
    <div class="banner-photo" role="img" aria-label="Offshore platform at dusk under a red sky with rising candlestick market chart"></div>
    <div class="banner-content">
      <div class="brand-name">PlexoVane<sup>®</sup></div>
      <h2 class="headline">RISK ANALYSIS SOFTWARE<br>FOR THE PETROLEUM PROFESSIONAL</h2>
      <p class="summary">PlexoVane<sup>®</sup> offers the petroleum industry a powerful, yet easy-to-use, well cost and scheduling risk analysis software. Our unique and intuitive user interface is designed specifically for the petroleum professional and offers an efficient and consistent way to create an accurate risked drilling and completion AFE.</p>
      <a class="cta" href="#">LEARN MORE</a>
    </div>
  </section>

  <section class="banner banner-3">
    <div class="banner-photo" role="img" aria-label="Offshore drilling rig beneath a stormy red sky with lightning"></div>
    <div class="banner-content">
      <div class="brand-name">PlexoVane<sup>®</sup></div>
      <h2 class="headline">RISK ANALYSIS SOFTWARE<br>FOR THE PETROLEUM PROFESSIONAL</h2>
      <p class="summary">PlexoVane<sup>®</sup> offers the petroleum industry a powerful, yet easy-to-use, well cost and scheduling risk analysis software. Our unique and intuitive user interface is designed specifically for the petroleum professional and offers an efficient and consistent way to create an accurate risked drilling and completion AFE.</p>
      <a class="cta" href="#">LEARN MORE</a>
    </div>
  </section>

  <section class="banner banner-4">
    <div class="banner-photo" role="img" aria-label="Lit offshore platform at night under a red overlay with candlestick chart and price figures"></div>
    <div class="banner-content">
      <div class="brand-name">PlexoVane<sup>®</sup></div>
      <h2 class="headline">RISK ANALYSIS SOFTWARE<br>FOR THE PETROLEUM PROFESSIONAL</h2>
      <p class="summary">PlexoVane<sup>®</sup> offers the petroleum industry a powerful, yet easy-to-use, well cost and scheduling risk analysis software. Our unique and intuitive user interface is designed specifically for the petroleum professional and offers an efficient and consistent way to create an accurate risked drilling and completion AFE.</p>
      <a class="cta" href="#">LEARN MORE</a>
    </div>
  </section>
</main>
</body>
</html>
```